CREST Academy Exhibit Booth Posters

My company is CREST Academy (a division of CREST for Growth). We are exhibiting in a month, and I need to re-do my exhibit booth posters. There will be a total of 4 posters needed. Sizes are below.
1) Top- 11 feet long X 12 inches wide (Try to match color scheme in example photo)
2) Center- 4 feet long X 2 feet wide (Chalkboard background)
3) Left- 18 inches long X 2 feet wide (Cork-board back ground with the use of push pins holding up post-it-notes, paper, etc.)
4) Right- 18 inches long X 2 feet wide (Cork-board back ground with the use of push pins holding up post-it-notes, paper, etc.)
I have attached a photo of my old booth. This will get you an idea of the size, color schemes, and more. I have created basic rendering of each poster. The content is important, but the look and design should be drastically improved.
The websites to look into for ideas are:
www.crestforgrowth.example
www.crestacademy.example
Updates
I've added a new file. It's a .JPG of the certification diploma. Thanks!
Target Market(s)
Business Owners, Managers, HR, Supervisors, Teens who want to boost their resume
Industry/Entity Type
It Company
Look and feel

```html
<!DOCTYPE html>
<html lang="en">
<head>
<meta charset="utf-8">
<title>CREST Academy – Center Booth Poster</title>
<link href="https://fonts.googleapis.com/css2?family=Fredoka:wght@600;700&family=Comic+Neue:wght@700&display=swap" rel="stylesheet">
<style>
  :root {
    --page: #d9d9d9;
    --chalk: #1b1d22;
    --chalk-light: #34373d;
    --frame: #ffffff;
    --blue: #1f6fd1;
    --blue-deep: #0b2f7a;
    --blue-pale: #9cc6f2;
    --orange-paper: #c9683c;
    --kraft: #c49a73;
    --note: #f7e9a8;
    --label: #f2f2f2;
    --tape: #111111;
    --ink: #ffffff;
    --ink-dark: #1a1a1a;
    --url-red: #d4141c;
    --pin-red: #d5261e;
    --pin-blue: #2e7fd6;
  }
  html, body { margin: 0; padding: 0; }
  body {
    width: 1200px; height: 848px; overflow: hidden;
    background: var(--page);
    font-family: "Comic Neue", "Comic Sans MS", cursive;
    font-weight: 700;
  }
  .poster {
    position: absolute; left: 40px; top: 144px;
    width: 1120px; height: 560px;
    background: var(--frame);
    box-shadow: 0 6px 18px rgba(0,0,0,.35);
  }
  .board {
    position: absolute; inset: 12px;
    overflow: hidden;
    background: radial-gradient(ellipse at 40% 40%, var(--chalk-light), var(--chalk) 75%);
  }
  .swoosh { position: absolute; inset: 0; width: 100%; height: 100%; }
  .piece { position: absolute; box-shadow: 2px 4px 8px rgba(0,0,0,.5); }
  .tape { position: absolute; background: var(--tape); opacity: .92; }

  .launch {
    left: 16px; top: 44px; width: 540px; height: 132px;
    background: var(--orange-paper); transform: rotate(-1deg);
    font-family: "Fredoka", sans-serif;
  }
  .launch-kicker { position: absolute; left: 26px; top: 18px; font-size: 30px; font-weight: 700; color: var(--ink); text-shadow: 2px 2px 2px rgba(0,0,0,.6); }
  .launch-title { position: absolute; left: 22px; top: 54px; font-size: 54px; font-weight: 700; color: var(--blue); white-space: nowrap; text-shadow: -2px -2px 0 #fff, 2px -2px 0 #fff, -2px 2px 0 #fff, 2px 2px 0 #fff, 4px 5px 4px rgba(0,0,0,.6); }

  .url {
    position: absolute; left: 590px; top: 20px;
    font-family: "Fredoka", sans-serif; font-weight: 700; font-size: 33px;
    color: var(--url-red); transform: rotate(-3deg); white-space: nowrap;
    text-shadow: -2px -2px 0 #fff, 2px -2px 0 #fff, -2px 2px 0 #fff, 2px 2px 0 #fff;
  }

  .brand {
    position: absolute; left: 400px; top: 220px; width: 300px;
    text-align: center; font-family: "Fredoka", sans-serif; font-weight: 700;
    color: var(--blue-pale); font-size: 58px; line-height: 1.05;
  }
  .brand-dot { width: 44px; height: 44px; border-radius: 50%; background: var(--blue); margin: 0 auto 14px; }

  .label {
    left: 30px; top: 226px; width: 250px; height: 96px;
    background: var(--label); transform: rotate(-12deg);
    text-align: center; color: var(--ink-dark); font-size: 21px; line-height: 1.1;
    padding-top: 14px; box-sizing: border-box; text-transform: uppercase;
  }

  .kraft { background: var(--kraft); }
  .skills { left: 42px; top: 298px; width: 370px; height: 220px; transform: rotate(-1deg); }
  .features { left: 690px; top: 262px; width: 380px; height: 236px; transform: rotate(-1deg); }

  .list { list-style: none; margin: 0; padding: 0; position: absolute; }
  .list li {
    display: flex; align-items: center; gap: 8px; white-space: nowrap;
    color: var(--ink); text-transform: uppercase; margin-bottom: 6px;
    text-shadow: -1.5px -1.5px 0 #222, 1.5px -1.5px 0 #222, -1.5px 1.5px 0 #222, 1.5px 1.5px 0 #222;
  }
  .list svg { flex: none; }
  .skills .list { left: 14px; top: 52px; }
  .skills li { font-size: 27px; }
  .skills li.small { font-size: 22px; }
  .more { position: absolute; right: 22px; bottom: 14px; color: var(--ink-dark); font-size: 22px; text-transform: uppercase; }
  .features .list { left: 20px; top: 22px; }
  .features li { font-size: 27px; }
  .features li.small { font-size: 20px; }

  .note {
    left: 730px; top: 112px; width: 300px; height: 150px;
    background: var(--note); transform: rotate(-3deg);
    text-align: center; color: var(--ink-dark); text-transform: uppercase;
    font-family: "Fredoka", sans-serif; font-weight: 600; font-size: 28px; line-height: 1.08;
    padding-top: 30px; box-sizing: border-box;
  }
</style>
</head>
<body>
<main class="poster" aria-label="CREST Academy center booth poster">
  <div class="board" role="img" aria-label="Chalkboard background with blue sweeping stripes">
    <svg class="swoosh" viewBox="0 0 1096 536" preserveAspectRatio="none" aria-hidden="true">
      <path d="M0 470 C300 430 700 470 1096 330 L1096 536 L0 536 Z" fill="var(--blue-deep)"/>
      <path d="M0 500 C320 460 720 500 1096 370" stroke="var(--blue)" stroke-width="10" fill="none"/>
      <path d="M0 515 C320 480 720 515 1096 395" stroke="var(--blue-pale)" stroke-width="4" fill="none"/>
      <path d="M760 60 C900 120 1000 200 1096 200" stroke="var(--blue)" stroke-width="22" fill="none" opacity=".8"/>
      <path d="M820 40 C940 90 1020 140 1096 140" stroke="var(--blue-pale)" stroke-width="6" fill="none" opacity=".7"/>
    </svg>
  </div>

  <div class="piece launch">
    <div class="launch-kicker">Launching...</div>
    <div class="launch-title">Thrive on the Job</div>
  </div>
  <div class="tape" style="left:220px;top:20px;width:120px;height:32px;transform:rotate(-4deg)"></div>

  <div class="url">www.crestacademy.example</div>

  <div class="brand">
    <div class="brand-dot"></div>
    CREST<br>Academy
  </div>

  <div class="piece kraft skills">
    <ul class="list">
      <li><svg width="26" height="26" viewBox="0 0 22 22"><circle cx="13" cy="8" r="7" fill="var(--pin-red)"/><line x1="9" y1="12" x2="2" y2="20" stroke="#888" stroke-width="2"/></svg>Customer Service</li>
      <li class="small"><svg width="26" height="26" viewBox="0 0 22 22"><circle cx="13" cy="8" r="7" fill="var(--pin-red)"/><line x1="9" y1="12" x2="2" y2="20" stroke="#888" stroke-width="2"/></svg>Communication</li>
      <li class="small"><svg width="26" height="26" viewBox="0 0 22 22"><circle cx="13" cy="8" r="7" fill="var(--pin-red)"/><line x1="9" y1="12" x2="2" y2="20" stroke="#888" stroke-width="2"/></svg>Social Media</li>
      <li><svg width="26" height="26" viewBox="0 0 22 22"><circle cx="13" cy="8" r="7" fill="var(--pin-red)"/><line x1="9" y1="12" x2="2" y2="20" stroke="#888" stroke-width="2"/></svg>Integrity</li>
    </ul>
    <div class="more">and more!</div>
  </div>

  <div class="piece label">Web-based training<br>for teens and<br>young adults</div>
  <div class="tape" style="left:20px;top:218px;width:70px;height:26px;transform:rotate(-12deg)"></div>

  <div class="piece note">30 Minute<br>Testing and<br>Certification</div>
  <div class="tape" style="left:820px;top:96px;width:110px;height:30px;transform:rotate(-4deg)"></div>

  <div class="piece kraft features">
    <ul class="list">
      <li class="small"><svg width="26" height="26" viewBox="0 0 22 22"><circle cx="13" cy="8" r="7" fill="var(--pin-blue)"/><line x1="9" y1="12" x2="2" y2="20" stroke="#888" stroke-width="2"/></svg>Industry Non-Specific</li>
      <li><svg width="26" height="26" viewBox="0 0 22 22"><circle cx="13" cy="8" r="7" fill="var(--pin-blue)"/><line x1="9" y1="12" x2="2" y2="20" stroke="#888" stroke-width="2"/></svg>Interactive</li>
      <li><svg width="26" height="26" viewBox="0 0 22 22"><circle cx="13" cy="8" r="7" fill="var(--pin-blue)"/><line x1="9" y1="12" x2="2" y2="20" stroke="#888" stroke-width="2"/></svg>Mobile Ready</li>
      <li><svg width="26" height="26" viewBox="0 0 22 22"><circle cx="13" cy="8" r="7" fill="var(--pin-blue)"/><line x1="9" y1="12" x2="2" y2="20" stroke="#888" stroke-width="2"/></svg>Peer to Peer</li>
      <li class="small"><svg width="26" height="26" viewBox="0 0 22 22"><circle cx="13" cy="8" r="7" fill="var(--pin-blue)"/><line x1="9" y1="12" x2="2" y2="20" stroke="#888" stroke-width="2"/></svg>Age Specific</li>
    </ul>
  </div>
  <div class="tape" style="left:1040px;top:250px;width:60px;height:26px;transform:rotate(20deg)"></div>
</main>
</body>
</html>
```